Luxury Wine Label for New Startup Winery

We need a wine label for our new winery startup. We have worked with a local designer but do not feel the resulting label / logo have the elevation required to present our brand as a luxury wine. Our winery is called "Harrowgate Vineyards" and we are focused on extremely high quality hand crafted artisan and estate wines from the Pacific Northwest.
We would like to see designs that utilize a tree line, or other imagery that represents the "Harrowgate" part of our company name. Another interesting feature could be wood grain.
A logo will be required based on your design so please design with this in mind:
This logo should be consistent with the wine bottle label design, and should be representative of our high end exclusive wine while giving a sense of place (Oregon/ Pacific Northwest.)
I will supply an image of the design we received from our local designer, PLEASE NOTE: in general we do like wood grain and tree line concepts but feel the execution was poorly done.
ATTN: Logo design should be suitable for use on: Bottles (Red wine/rose/white wine), Bussiness cards, vehicle signage, business signage, etc
P.S.:
If you have a design that is not outside the box we are still interested in seeing it.
Label is for a burgundy style bottle with a label height of 3.5 - 4" and a width of 3.5-4"
any label <= 4"x4" and >=3.5"x3.5" will be acceptable:
HOWEVER Width should be greater than or equal to height due to the bottle format
Target Market(s)
Wine enthusiasts with adequate discretionary budgets to afford $100 bottles of wine.
Industry/Entity Type
Wine / Winery
Requirements
Must have
- A sense of luxury, a feel of exclusivity, and a theme consistent with our product and brand name
Nice to have
- Tree line, wood grain or other wood themes. Serif fonts
Should not have
- anything cheesy, off topic, hard to read script fonts or anything that makes the label hard to read from a few feet away or too busy

```html
<!DOCTYPE html>
<html lang="en">
<head>
<meta charset="utf-8">
<title>Harrowgate Vineyards – Syrah Label</title>
<link href="https://fonts.googleapis.com/css2?family=Cinzel:wght@400;500&family=Raleway:wght@400&display=swap" rel="stylesheet">
<style>
  :root {
    --page: #ffffff;
    --label-dark: #1f1917;
    --ivory: #f3efe8;
    --silver-light: #d9d9dc;
    --silver-dark: #6f6f74;
    --region-red: #c8382a;
    --gold: #c49a4c;
    --gold-line: #b8913f;
    --wood-dark: #3b2a20;
    --wood-mid: #6a5140;
    --wood-light: #8a6d58;
  }
  * { margin: 0; padding: 0; box-sizing: border-box; }
  html, body {
    width: 840px;
    height: 1200px;
    overflow: hidden;
    background: var(--page);
  }
  .canvas {
    position: relative;
    width: 840px;
    height: 1200px;
  }
  .label {
    position: absolute;
    left: 45px;
    top: 178px;
    width: 750px;
  }
  .label-main {
    position: relative;
    height: 603px;
    background: var(--label-dark);
    text-align: center;
  }
  .rule {
    position: absolute;
    left: 31px;
    right: 31px;
    height: 3px;
    background: linear-gradient(90deg, var(--silver-dark), var(--silver-light) 30%, var(--silver-light) 70%, var(--silver-dark));
  }
  .rule-top { top: 26px; }
  .rule-bottom { top: 577px; }
  .brand-mark {
    position: absolute;
    left: 50%;
    top: 150px;
    width: 22px;
    height: 22px;
    margin-left: -11px;
    background: var(--gold);
  }
  .brand-name {
    position: absolute;
    left: 0;
    right: 0;
    top: 262px;
    font-family: "Cinzel", serif;
    font-weight: 500;
    color: var(--ivory);
    line-height: 1;
  }
  .brand-name .primary {
    display: block;
    font-size: 66px;
    letter-spacing: 3px;
  }
  .brand-name .secondary {
    display: block;
    margin-top: 22px;
    font-size: 30px;
    letter-spacing: 4px;
  }
  .region {
    position: absolute;
    left: 0;
    right: 0;
    top: 490px;
    font-family: "Raleway", sans-serif;
    font-size: 33px;
    color: var(--region-red);
    letter-spacing: 0;
    line-height: 1;
  }
  .varietal-band {
    margin-top: 42px;
  }
  .wood-strip {
    height: 45px;
    background: linear-gradient(180deg, var(--wood-mid), var(--wood-light) 35%, var(--wood-dark) 60%, var(--wood-mid));
  }
  .varietal {
    height: 110px;
    background: var(--label-dark);
    border-top: 3px solid var(--gold-line);
    border-bottom: 3px solid var(--gold-line);
    display: flex;
    align-items: center;
    justify-content: center;
    font-family: "Cinzel", serif;
    font-weight: 500;
    font-size: 48px;
    letter-spacing: 3px;
    color: var(--gold);
  }
</style>
</head>
<body>
<main class="canvas">
  <section class="label">
    <div class="label-main">
      <span class="rule rule-top"></span>
      <span class="brand-mark"></span>
      <h1 class="brand-name">
        <span class="primary">HARROWGATE</span>
        <span class="secondary">VINEYARDS</span>
      </h1>
      <p class="region">WILLAMETTE VALLEY</p>
      <span class="rule rule-bottom"></span>
    </div>
    <div class="varietal-band">
      <div class="wood-strip" role="img" aria-label="Wood grain band"></div>
      <p class="varietal">SYRAH</p>
      <div class="wood-strip" role="img" aria-label="Wood grain band"></div>
    </div>
  </section>
</main>
</body>
</html>
```